Corvella Web Design Project

I am attaching my logo so I need to see applied to the website developed by you guys!!
Tbahks!!
Marcello
This is the DNA of the company
Flat and dynamic organization - Informal and respectful social approac
Innovative - Always striving for the best solution
Reliability and Quality - The value of our name
Flexibility - Ability to handle new requirements and unforeseen events
Simplicity - Technology must serve – NOT rule!
Cooperative Relations - The synergy that makes 1+1=3
We still don´t have our logo as we have another open project on artbazaar
Our company won´t be selling this equipment but providing welding services for shipyard industry, as you can see on the website below.
www.velmorix.com
Updates
Project Deadline Extended
Reason: Hi webdesigners,
I will be deciding my logo by this weekend as soon as I have decided I will post my logo to see it applied to your design!!!
Thanks
Marcello
I just Sent my logo for your attention!!!!
Industry/Entity Type
Welding
Look and feel
Each slider illustrates characteristics of the customer's brand and the style your logo design should communicate.

```html
<!DOCTYPE html>
<html lang="en">
<head>
<meta charset="utf-8">
<title>Corvella – Welding Services</title>
<link rel="stylesheet" href="https://fonts.googleapis.com/css2?family=Lato:wght@400;700&family=Ubuntu:wght@500&display=swap">
<style>
:root{
  --navy:#0a2a4a;
  --blue:#0e4d7e;
  --btn:#1a7fc0;
  --text:#555;
  --page:#f3f3f3;
  --footer:#2a2a2a;
  --line:#dcdcdc;
}
*{box-sizing:border-box;margin:0;padding:0}
html,body{width:890px;height:1200px;overflow:hidden}
body{position:relative;background:var(--page);font-family:"Lato",sans-serif;color:var(--text)}
.abs{position:absolute}
.topbar{left:0;top:0;width:890px;height:32px;background:var(--navy);color:#fff;font-size:11px}
.topbar .item{position:absolute;top:9px;display:flex;align-items:center;gap:7px}
.topbar .sep{position:absolute;left:644px;top:7px;width:1px;height:18px;background:#6d8399}
.brand{left:74px;top:62px;width:156px;height:50px;border:3px solid var(--blue);display:flex;align-items:center;justify-content:center;font-weight:700;font-size:26px;color:var(--blue)}
.brand-sep{left:248px;top:60px;width:1px;height:58px;background:#bbb}
.tagline{left:264px;top:77px;font-size:17px;color:#333}
.search{left:658px;top:74px;width:141px;height:28px;border:1px solid #ccc;border-radius:3px;background:#f7f7f7;font-size:10px;font-style:italic;color:#888;padding:8px 10px}
.search svg{position:absolute;right:10px;top:6px}
.nav{left:74px;top:139px;width:744px;height:36px;background:var(--blue);border-radius:4px;display:flex;justify-content:center;align-items:center;gap:28px;color:#fff;font-weight:700;font-size:12.5px}
.slider{left:74px;top:190px;width:744px;height:290px;box-shadow:0 10px 14px -8px rgba(0,0,0,.35)}
.slide-photo{position:absolute;left:0;top:0;width:527px;height:290px;background:linear-gradient(135deg,#c9ccd2 0%,#4158b8 35%,#8b8fa3 60%,#3d4a8e 80%,#2b2b33 100%)}
.slide-panel{position:absolute;left:527px;top:0;width:217px;height:290px;background:linear-gradient(180deg,#3a4a3a 0%,#141414 40%,#0b0b0b 100%);color:#fff;padding:0 14px 0 6px}
.slide-panel h2{font-family:"Ubuntu",sans-serif;font-weight:500;font-size:18px;text-align:right;margin-top:47px}
.slide-panel .by{font-size:8px;text-align:right;margin-top:2px}
.slide-panel p{font-size:7px;line-height:8.6px;margin-top:16px}
.slide-panel ul{list-style:none;margin-top:10px;padding-left:16px;font-size:7px;line-height:9px}
.slide-panel li{position:relative}
.slide-panel li svg{position:absolute;left:-13px;top:1px}
.btn{display:inline-block;background:var(--btn);color:#fff;font-size:8.5px;font-weight:700;padding:4px 6px;border-radius:3px;box-shadow:0 2px 3px rgba(0,0,0,.3)}
.slide-panel .btn{position:absolute;left:6px;top:219px}
.arrows{position:absolute;left:7px;top:246px;display:flex;gap:4px}
.main{left:74px;top:529px;width:744px;height:587px;background:#fff;border:1px solid var(--line)}
.footer{left:0;top:1071px;width:890px;height:129px;background:var(--footer)}
h3{color:var(--blue);font-weight:400;font-size:19px}
.about h3{position:absolute;left:101px;top:540px}
.about-text{left:101px;top:569px;width:410px;font-size:11px;line-height:11.3px;color:#666}
.about-text p+p{margin-top:11px}
.about .btn{position:absolute;left:101px;top:675px}
.about-img{left:573px;top:540px;width:189px;height:159px;border:2px solid #ccc;background:radial-gradient(circle at 55% 60%,#e0c21a 0%,#a88a10 40%,#5c5a4e 75%,#3a3a3a 100%)}
.rule{left:101px;top:724px;width:661px;height:1px;background:var(--line)}
.thumb{top:752px;width:143px;height:131px;box-shadow:0 5px 6px -4px rgba(0,0,0,.4)}
.thumb .label{position:absolute;left:0;bottom:0;width:100%;height:19px;background:rgba(0,0,0,.55);color:#fff;font-size:8.5px;font-weight:700;padding:4px 5px}
.videos h3{position:absolute;left:101px;top:931px}
.video{top:977px;width:180px;height:50px}
.video .vthumb{position:absolute;left:0;top:0;width:62px;height:48px;border:1px solid #aaa;background:linear-gradient(135deg,#8a8a8a,#3c3c3c)}
.video .vthumb svg{position:absolute;left:22px;top:15px}
.video h4{position:absolute;left:70px;top:0;font-weight:400;font-size:11px;color:#333}
.video p{position:absolute;left:70px;top:18px;width:102px;font-size:6.5px;line-height:8px;color:#555}
.vsep{left:290px;top:971px;width:1px;height:56px;background:var(--line)}
.vnav{left:101px;top:1045px;display:flex;gap:4px}
.news h3{position:absolute;left:543px;top:931px}
.news-item{left:543px;width:175px;height:50px}
.date{position:absolute;left:0;top:0;width:29px;height:24px;border:1px solid #ccc;background:#f3f3f3;text-align:center;font-size:10px;color:var(--blue)}
.date span{display:block;background:var(--blue);color:#fff;font-size:6.5px;height:9px;line-height:9px}
.news-item h5{position:absolute;left:39px;top:-2px;font-weight:400;font-size:9px;color:var(--blue)}
.news-item p{position:absolute;left:39px;top:12px;width:120px;font-size:5.5px;line-height:8px;color:#777}
.news-item p b{font-weight:400;color:var(--blue)}
.news-sep{left:543px;top:1021px;width:175px;height:1px;background:var(--line)}
.foot-links{left:73px;top:1136px;display:flex;gap:22px;color:#ddd;font-size:10px}
.copy{left:73px;top:1167px;font-size:7px;color:#bbb}
.follow{left:722px;top:1129px;font-size:12px;font-weight:700;color:#fff}
.social{top:1152px;width:24px;height:24px;border-radius:2px}
</style>
</head>
<body>

<div class="abs topbar">
  <div class="item" style="left:525px">
    <svg width="12" height="12" viewBox="0 0 12 12"><rect width="12" height="12" rx="2" fill="#fff"/><path d="M3.5 2.5l1.6 1.8-.8 1.2c.5 1 1.2 1.7 2.2 2.2l1.2-.8 1.8 1.6-.8 1.2C5.6 9.5 2.5 6.4 2.3 3.3z" fill="#0a2a4a"/></svg>
    (012) 555 -0147
  </div>
  <div class="sep"></div>
  <div class="item" style="left:663px">
    <svg width="14" height="10" viewBox="0 0 14 10"><rect width="14" height="10" fill="#fff"/><path d="M0 0l7 5.5L14 0" fill="none" stroke="#0a2a4a" stroke-width="1.2"/></svg>
    info@corvella.com
  </div>
</div>

<div class="abs brand">Corvella</div>
<div class="abs brand-sep"></div>
<div class="abs tagline">Put your tagline here please</div>
<div class="abs search">Search site
  <svg width="16" height="16" viewBox="0 0 16 16"><circle cx="6.5" cy="6.5" r="5" fill="none" stroke="#999" stroke-width="2"/><path d="M10 10l5 5" stroke="#999" stroke-width="2.4"/></svg>
</div>

<nav class="abs nav">
  <span>Home</span><span>About Us</span><span>Competence</span><span>Case Story</span><span>Products</span><span>Videos</span><span>Downloads</span>
</nav>

<section class="abs slider">
  <div class="slide-photo" role="img" aria-label="Blue industrial welding robots on display at a trade fair"></div>
  <div class="slide-panel">
    <h2>Welding Automation</h2>
    <div class="by">- Velmorix featuring AXLP</div>
    <p>With the innovation; AXLP (Automated Cross-Line Path Technology) Velmorix from Denmark has set new standards for future welding automation technology world wide. Key points are:</p>
    <ul>
      <li><svg width="8" height="7" viewBox="0 0 8 7"><path d="M1 3.5l2 2L7 1" fill="none" stroke="#fff" stroke-width="1.5"/></svg>Self programming robot intelligens</li>
      <li><svg width="8" height="7" viewBox="0 0 8 7"><path d="M1 3.5l2 2L7 1" fill="none" stroke="#fff" stroke-width="1.5"/></svg>Very simple and intuitive operation</li>
      <li><svg width="8" height="7" viewBox="0 0 8 7"><path d="M1 3.5l2 2L7 1" fill="none" stroke="#fff" stroke-width="1.5"/></svg>No engineering back-up required</li>
      <li><svg width="8" height="7" viewBox="0 0 8 7"><path d="M1 3.5l2 2L7 1" fill="none" stroke="#fff" stroke-width="1.5"/></svg>Ease of installation and implementation</li>
      <li><svg width="8" height="7" viewBox="0 0 8 7"><path d="M1 3.5l2 2L7 1" fill="none" stroke="#fff" stroke-width="1.5"/></svg>No CAD or drawing interface needed…</li>
    </ul>
    <span class="btn">Read More</span>
    <div class="arrows">
      <svg width="13" height="13" viewBox="0 0 13 13"><circle cx="6.5" cy="6.5" r="6.5" fill="#fff"/><path d="M7.8 3.5L4.8 6.5l3 3" fill="none" stroke="#111" stroke-width="1.6"/></svg>
      <svg width="13" height="13" viewBox="0 0 13 13"><circle cx="6.5" cy="6.5" r="6.5" fill="#fff"/><path d="M5.2 3.5l3 3-3 3" fill="none" stroke="#111" stroke-width="1.6"/></svg>
    </div>
  </div>
</section>

<div class="abs footer"></div>
<div class="abs main"></div>

<section class="about">
  <h3>About Our Company</h3>
  <div class="abs about-text">
    <p>Lorem ipsum dolor sit amet, consectetur adipisicing elit, sed do eiusmod tempor incididunt ut labore et dolore magna aliqua. Ut enim ad minim veniam, quis nostrud exercitation ullamco laboris nisi ut aliquip ex ea commodo consequat.</p>
    <p>Duis aute irure dolor in reprehenderit in voluptate velit esse cillum dolore eu fugiat nulla pariatur. Excepteur sint occaecat cupidatat non proident, sunt in culpa qui officia deserunt mollit anim id est laborum. Sed ut perspiciatis unde omnis iste natus. error sit voluptatem accusantium.</p>
  </div>
  <span class="btn">Read More</span>
  <div class="abs about-img" role="img" aria-label="Welding robot arm working with bright yellow welding glow"></div>
</section>

<div class="abs rule"></div>

<div class="abs thumb" style="left:102px;background:linear-gradient(135deg,#c7d0da,#3b55b5 50%,#5a5f70)" role="img" aria-label="Row of blue welding robots with control cabinets"><div class="label">Label Here</div></div>
<div class="abs thumb" style="left:275px;background:linear-gradient(160deg,#4a3a28,#c9b690 45%,#2e2418)" role="img" aria-label="Automated welding line with sparks in a dark workshop"><div class="label">Label Here</div></div>
<div class="abs thumb" style="left:448px;background:linear-gradient(135deg,#d4d8dc,#4a5fb8 50%,#6a6e78)" role="img" aria-label="Blue welding robots in an exhibition hall"><div class="label">Label Here</div></div>
<div class="abs thumb" style="left:621px;background:linear-gradient(135deg,#e8b89a,#d8662a 50%,#6a5040)" role="img" aria-label="Orange robot arms on a factory production line"><div class="label">Label Here</div></div>

<section class="videos">
  <h3>Videos</h3>
  <div class="abs video" style="left:101px">
    <div class="vthumb" role="img" aria-label="Welding video preview"><svg width="18" height="18" viewBox="0 0 18 18"><circle cx="9" cy="9" r="9" fill="#fff"/><path d="M7 5l6 4-6 4z" fill="#333"/></svg></div>
    <h4>Lorem Ipsum</h4>
    <p>Apisicing elit, sed do eiusmod tempor incididunt ut labore et dolore magna aliqua.</p>
  </div>
  <div class="abs vsep"></div>
  <div class="abs video" style="left:310px">
    <div class="vthumb" role="img" aria-label="Welding video preview"><svg width="18" height="18" viewBox="0 0 18 18"><circle cx="9" cy="9" r="9" fill="#fff"/><path d="M7 5l6 4-6 4z" fill="#333"/></svg></div>
    <h4>Lorem Ipsum</h4>
    <p>Apisicing elit, sed do eiusmod tempor incididunt ut labore et dolore magna aliqua.</p>
  </div>
  <div class="abs vnav">
    <svg width="9" height="11" viewBox="0 0 9 11"><path d="M9 0v11L0 5.5z" fill="#0e4d7e"/></svg>
    <svg width="9" height="11" viewBox="0 0 9 11"><path d="M0 0v11l9-5.5z" fill="#0e4d7e"/></svg>
  </div>
</section>

<section class="news">
  <h3>Recent News</h3>
  <div class="abs news-item" style="top:974px">
    <div class="date"><span>Aug</span>15</div>
    <h5>Adipisicing elit sed</h5>
    <p>Eiusmod tempor incididunt ut labore et dolore magna aliqua. Ut enim ad minim veniam, quis nostrud exercitation ullam ...<b>[Read More]</b></p>
  </div>
  <div class="abs news-sep"></div>
  <div class="abs news-item" style="top:1037px">
    <div class="date"><span>Aug</span>15</div>
    <h5>Adipisicing elit sed</h5>
    <p>Eiusmod tempor incididunt ut labore et dolore magna aliqua. Ut enim ad minim veniam, quis nostrud exercitation ullam ...<b>[Read More]</b></p>
  </div>
</section>

<nav class="abs foot-links">
  <span>Home</span><span>About Us</span><span>Competence</span><span>Case Story</span><span>Products</span><span>Videos</span><span>Downloads</span>
</nav>
<div class="abs copy">Copyright©corvella.2014. All Rights Reserved</div>
<div class="abs follow">Follow Us</div>
<div class="abs social" style="left:723px;background:#1da1e0" aria-label="Social profile"></div>
<div class="abs social" style="left:758px;background:#3b5a9a" aria-label="Social profile"></div>
<div class="abs social" style="left:793px;background:#d9442f" aria-label="Social profile"></div>

</body>
</html>
```